We are a music event management company based out of Syracuse, NY but we do business in multiple areas like the mid-west and Florida.

Our primary events revolve around the Electronic Dance Music scene. (acts like Brightmoor, Coastal Pulse Syndicate, Dorian Falk)

We would like a clean cut business card with Voltarine written on the back. In Voltarine we would like the u to be shaped like a sixteenth note. The colors green and silver would be nice to see somehow but not necessary. Feel free to play around with it and have fun because that's what our business is about, Having Fun!

Some similar examples for reference would be the Neon Orchard or Glowing Tulip Jubilee website.

Our goal is to provide people with an experience, not just a concert. There is a difference.

```html
<!DOCTYPE html>
<html lang="en">
<head>
<meta charset="utf-8">
<title>Voltarine Business Card</title>
<link rel="stylesheet" href="https://fonts.googleapis.com/css2?family=Lato:wght@300;400;700&display=swap">
<style>
  :root {
    --backdrop: #ece4d6;
    --green-light: #62a887;
    --green-mid: #2e7a56;
    --green-dark: #0a4a2c;
    --silver-light: #f2f2f2;
    --silver-mid: #b9bcbd;
    --silver-dark: #6f7374;
    --ink: #ffffff;
    --ink-soft: rgba(255,255,255,0.8);
  }
  * { box-sizing: border-box; margin: 0; padding: 0; }
  html, body { width: 1200px; height: 1000px; overflow: hidden; }
  body {
    background: var(--backdrop);
    font-family: "Lato", sans-serif;
    color: var(--ink);
    position: relative;
  }
  .card {
    position: absolute;
    top: 340px;
    width: 540px;
    height: 310px;
    border-radius: 6px;
    overflow: hidden;
    background: radial-gradient(ellipse 62% 70% at 50% 50%, var(--green-light) 0%, var(--green-mid) 45%, var(--green-dark) 100%);
    box-shadow: 0 6px 14px rgba(0,0,0,0.28);
  }
  .card--front { left: 40px; }
  .card--back { left: 620px; }
  .card__band {
    position: absolute; top: 0; left: 0; right: 0; height: 12px;
    background: linear-gradient(90deg, var(--silver-dark) 0%, var(--silver-light) 30%, var(--silver-mid) 55%, var(--silver-light) 80%, var(--silver-dark) 100%);
  }
  .brand {
    font-weight: 300;
    color: var(--ink);
    letter-spacing: 0.5px;
    line-height: 1;
  }
  .card--front .brand { position: absolute; left: 28px; top: 30px; font-size: 34px; }
  .card--back .brand {
    position: absolute; left: 0; right: 0; top: 132px;
    text-align: center; font-size: 44px;
  }
  .holder { position: absolute; right: 26px; top: 26px; text-align: right; }
  .holder__name { font-weight: 700; font-size: 21px; line-height: 1.1; }
  .holder__title { font-weight: 300; font-size: 12px; color: var(--ink-soft); margin-top: 2px; }
  .contacts { position: absolute; left: 24px; bottom: 22px; list-style: none; }
  .contacts li {
    display: flex; align-items: center; gap: 10px;
    font-weight: 300; font-size: 15.5px; height: 26.5px; white-space: nowrap;
  }
  .contacts svg { width: 19px; height: 19px; flex: none; }
</style>
</head>
<body>
  <section class="card card--front">
    <div class="card__band"></div>
    <div class="brand">Voltarine</div>
    <div class="holder">
      <div class="holder__name">Marcus T</div>
      <div class="holder__title">Delbrook III CEO</div>
    </div>
    <ul class="contacts">
      <li>
        <svg viewBox="0 0 20 20" aria-hidden="true"><circle cx="10" cy="10" r="9" fill="none" stroke="#fff" stroke-width="1.4"/><path d="M7 5.5c-1 .6-1.4 1.6-1 2.8 1 2.7 3 4.7 5.7 5.7 1.2.4 2.2 0 2.8-1l-1.8-1.6-1.2.8c-1.2-.6-2.1-1.5-2.7-2.7l.8-1.2z" fill="#fff"/></svg>
        315-555-0142
      </li>
      <li>
        <svg viewBox="0 0 20 20" aria-hidden="true"><circle cx="10" cy="10" r="9" fill="#fff"/><text x="10" y="14" text-anchor="middle" font-family="Lato, sans-serif" font-weight="700" font-size="12" fill="#1d5f40">@</text></svg>
        marcus@voltarineny.com
      </li>
      <li>
        <svg viewBox="0 0 20 20" aria-hidden="true"><circle cx="10" cy="10" r="9" fill="#fff"/><g fill="none" stroke="#1d5f40" stroke-width="1"><circle cx="10" cy="10" r="6"/><ellipse cx="10" cy="10" rx="2.6" ry="6"/><path d="M4 10h12M5 7h10M5 13h10"/></g></svg>
        www.voltarineny.com
      </li>
      <li>
        <svg viewBox="0 0 20 20" aria-hidden="true"><circle cx="10" cy="10" r="9" fill="#fff"/><rect x="5" y="6.5" width="10" height="7" fill="none" stroke="#1d5f40" stroke-width="1.2"/><path d="M5 6.5l5 4 5-4" fill="none" stroke="#1d5f40" stroke-width="1.2"/></svg>
        PO box 847, Ashbrook, NY 10485
      </li>
    </ul>
  </section>

  <section class="card card--back">
    <div class="card__band"></div>
    <div class="brand">Voltarine</div>
  </section>
</body>
</html>
```